Civic Holdwell Business Card

We are looking to design new business cards for our company. We have two office locations and would like to have both full addresses on the card. Each address needs two lines for the building name and street address and a line or two for the city, state and zip code. There should be a place for 2-3 phone numbers. The addresses and phone numbers are at the bottom of this description. We also need a place to put our company website and one email address. Our logo is attached.
We would like the card to be two sided. The back of the card should have a blue background with some part of our logo design on it. We would like the full logo on the front of the card as well. The front of the card should have a white background with the blue logo. We are open to listing our addresses on the front or the back of the card. The person who designed our logo gave us an excellent business card idea that we really liked. I have attached a picture of his business card idea so that we can build off of it.
Addresses:
The Tanner Hall
2184 17th Street NW
Washington, DC 20007
Marlow Crest Tower
410 Dorsen Avenue #2215
Miami, FL 33131
Phone Numbers: (202) 555-0148
(202) 555-0193
Website: www.civicholdwell.example

```html
<!DOCTYPE html>
<html lang="en">
<head>
<meta charset="utf-8">
<title>Civic Holdwell Business Card</title>
<link href="https://fonts.googleapis.com/css2?family=Exo+2:wght@400&display=swap" rel="stylesheet">
<style>
  :root {
    --page-bg: #ecebe8;
    --card-white: #ffffff;
    --brand-blue: #27317f;
    --text-grey: #3f3f46;
    --on-blue: #ffffff;
  }
  html, body {
    margin: 0;
    padding: 0;
    width: 1200px;
    height: 841px;
    overflow: hidden;
    background: var(--page-bg);
    font-family: "Exo 2", sans-serif;
  }
  .card-set {
    position: absolute;
    top: 266px;
    left: 40px;
    display: flex;
    gap: 40px;
  }
  .card {
    position: relative;
    width: 540px;
    height: 309px;
    box-sizing: border-box;
    box-shadow: 0 6px 18px rgba(0,0,0,0.16);
  }
  .card-front {
    background: var(--card-white);
    padding: 26px 30px;
  }
  .card-back {
    background: var(--brand-blue);
  }
  .brand {
    display: flex;
    align-items: center;
    gap: 8px;
    color: var(--brand-blue);
  }
  .brand-mark {
    width: 40px;
    height: 40px;
    background: var(--brand-blue);
  }
  .brand-name {
    font-size: 30px;
    line-height: 1;
    letter-spacing: 2px;
    text-transform: uppercase;
  }
  .contact {
    margin-top: 18px;
    font-size: 13.5px;
    line-height: 1.4;
    color: var(--text-grey);
  }
  .office {
    margin: 0 0 14px;
    font-style: normal;
  }
  .phone-list {
    margin: 0;
    padding: 0;
    list-style: none;
  }
  .label {
    color: var(--brand-blue);
  }
  .online {
    position: absolute;
    right: 30px;
    bottom: 26px;
    margin: 0;
    padding: 0;
    list-style: none;
    text-align: right;
    font-size: 13.5px;
    line-height: 1.4;
    color: var(--text-grey);
  }
  .back-name {
    position: absolute;
    right: 44px;
    top: 128px;
    color: var(--on-blue);
    font-size: 34px;
    letter-spacing: 3px;
    text-transform: uppercase;
  }
</style>
</head>
<body>
  <main class="card-set">
    <section class="card card-front" aria-label="Card front">
      <div class="brand">
        <span class="brand-mark"></span>
        <span class="brand-name">Civic Holdwell</span>
      </div>
      <div class="contact">
        <address class="office">
          The Tanner Hall<br>
          2184 17th Street NW<br>
          Washington, DC 20007
        </address>
        <address class="office">
          Marlow Crest Tower<br>
          410 Dorsen Avenue<br>
          #2215 Miami, FL 33131
        </address>
        <ul class="phone-list">
          <li><span class="label">Phone:</span> (202) 555-0148</li>
          <li><span class="label">Phone:</span> (202) 555-0193</li>
        </ul>
      </div>
      <ul class="online">
        <li><span class="label">Email:</span> info@civicholdwell.example</li>
        <li><span class="label">Web:</span> www.civicholdwell.example</li>
      </ul>
    </section>
    <section class="card card-back" aria-label="Card back">
      <span class="back-name">Civic Holdwell</span>
    </section>
  </main>
</body>
</html>
```